New Business Card Design Project

New business card design required for an electrical business in Australia. Offering quality electrical services including design and installation. Electrical services offered are domestic, commercial and industrial. Also meets all the air conditioning installation and maintenance needs.

Target Market(s)

The business is sleek, professional and caters primarily to wealthy clients and government contracts looking for exceptional, tailored service.

Industry/Entity Type

Electrical

Contact Information for Business Card

Gareth Pollwick (Director)
0438 692 174
admin@rvoelectrical.com.au
www.rvoelectrical.com.au

Font styles to use
Sans Serif

Requirements
Must have
• The business card must show the license number - 64139 to comply with legislation.
Nice to have
• The logo colours and fonts could be incorporated into the design if the designer sees fit. We are open to new ideas and welcome creativity. The logo style guide is attached for reference if required.

```html
<!DOCTYPE html>
<html lang="en">
<head>
<meta charset="utf-8">
<title>RVO Electrical – Business Card</title>
<link rel="stylesheet" href="https://fonts.googleapis.com/css2?family=Roboto:wght@300;400;700&display=swap">
<style>
  :root {
    --backdrop: #808080;
    --navy: #0f2b54;
    --navy-soft: #16365f;
    --white: #ffffff;
    --ink-grey: #4a4a4a;
    --cord-grey: #5c5c5c;
    --shadow: rgba(0, 0, 0, 0.45);
  }
  * { box-sizing: border-box; margin: 0; padding: 0; }
  html, body {
    width: 1200px; height: 801px; overflow: hidden;
    background: var(--backdrop);
    font-family: "Roboto", Arial, sans-serif;
  }
  .card {
    position: absolute;
    left: 379px;
    width: 442px; height: 264px;
    overflow: hidden;
    box-shadow: 2px 2px 1px var(--shadow);
  }
  .card--front { top: 131px; background: var(--white); }
  .card--back { top: 430px; background: var(--navy); }

  /* front */
  .side-band {
    position: absolute; left: 0; top: 0;
    width: 55px; height: 100%;
    background: var(--navy);
  }
  .pendant-cord {
    position: absolute; left: 56px; top: 0;
    width: 2px; height: 170px;
    background: var(--cord-grey);
  }
  .pendant-lamp {
    position: absolute; left: 22px; top: 168px;
    width: 72px; height: 96px;
    border-radius: 36px 36px 36px 36px / 40px 40px 50px 50px;
    background: #e9ebee;
  }
  .brand {
    position: absolute; color: var(--navy); font-weight: 400;
    line-height: 1;
  }
  .brand__name { display: block; }
  .brand__sub { display: block; }
  .card--front .brand { left: 78px; top: 36px; }
  .card--front .brand__name { font-size: 50px; letter-spacing: 1px; }
  .card--front .brand__sub { font-size: 13px; letter-spacing: 3px; margin: 4px 0 0 58px; }

  .licence {
    position: absolute; right: 20px; top: 47px;
    font-size: 11px; color: var(--navy);
  }
  .contact { position: absolute; left: 135px; top: 136px; }
  .contact__name {
    font-size: 16px; font-weight: 700; color: var(--navy);
    letter-spacing: 0.2px; line-height: 1;
  }
  .contact__role { font-size: 12px; color: var(--ink-grey); margin-top: 3px; }
  .contact__list { list-style: none; margin-top: 8px; }
  .contact__item {
    display: flex; align-items: center; gap: 3px;
    font-size: 12px; color: var(--ink-grey); line-height: 15.5px;
  }
  .contact__item svg { width: 11px; height: 11px; flex: none; fill: var(--navy); }

  /* back */
  .bulb-field {
    position: absolute; inset: 0;
    background: linear-gradient(180deg, var(--navy) 0%, var(--navy-soft) 55%, var(--navy) 100%);
  }
  .card--back .brand { color: var(--white); left: 84px; top: 74px; }
  .card--back .brand__name { font-size: 88px; letter-spacing: 2px; }
  .card--back .brand__sub { font-size: 22px; letter-spacing: 5px; margin: 4px 0 0 103px; font-weight: 400; }
</style>
</head>
<body>

<section class="card card--front">
  <div class="side-band"></div>
  <div class="pendant-cord"></div>
  <div class="pendant-lamp" role="img" aria-label="Line illustration of a hanging light bulb"></div>

  <div class="brand">
    <span class="brand__name">RVO</span>
    <span class="brand__sub">ELECTRICAL</span>
  </div>

  <p class="licence">LIC NO: 64139</p>

  <div class="contact">
    <p class="contact__name">GARETH POLLWICK</p>
    <p class="contact__role">Director</p>
    <ul class="contact__list">
      <li class="contact__item">
        <svg viewBox="0 0 24 24" aria-hidden="true"><path d="M6.6 10.8a15.1 15.1 0 0 0 6.6 6.6l2.2-2.2a1 1 0 0 1 1-.25 11.4 11.4 0 0 0 3.6.57 1 1 0 0 1 1 1V20a1 1 0 0 1-1 1A17 17 0 0 1 3 4a1 1 0 0 1 1-1h3.5a1 1 0 0 1 1 1c0 1.25.2 2.45.57 3.57a1 1 0 0 1-.25 1z"/></svg>
        0438 692 174
      </li>
      <li class="contact__item">
        <svg viewBox="0 0 24 24" aria-hidden="true"><path d="M2 5h20v14H2z M2 5l10 8 10-8" fill="var(--navy)" stroke="#fff" stroke-width="1.5"/></svg>
        admin@rvoelectrical.com.au
      </li>
      <li class="contact__item">
        <svg viewBox="0 0 24 24" aria-hidden="true"><circle cx="12" cy="12" r="9.5" fill="none" stroke="var(--navy)" stroke-width="2"/><path d="M2.5 12h19M12 2.5v19M5 7h14M5 17h14" stroke="var(--navy)" stroke-width="1.5" fill="none"/><ellipse cx="12" cy="12" rx="4.5" ry="9.5" fill="none" stroke="var(--navy)" stroke-width="1.5"/></svg>
        www.rvoelectrical.com.au
      </li>
    </ul>
  </div>
</section>

<section class="card card--back">
  <div class="bulb-field" role="img" aria-label="Faint pattern of hanging light bulbs on cords"></div>
  <div class="brand">
    <span class="brand__name">RVO</span>
    <span class="brand__sub">ELECTRICAL</span>
  </div>
</section>

</body>
</html>
```